New branding for a sponsored social ad network

We're seeking a new corporate branding for our sponsored social ad network.

We deliver over 6 million clicks per day off of lumiport and zonvel to brands, game and app companies, musicians and a host of other content and product producers seeking to get the right eyeballs on their content.

Our current design and a little information about our company can be seen at http://qv.lo/pmTHza

An example of a competitor site we'd like to closely resemble in look and feel can be seen at http://qv.lo/82GvR4k

Industry/Entity Type

It Company

```html
<!DOCTYPE html>
<html lang="en">
<head>
<meta charset="utf-8">
<title>Chatterly — sponsored social traffic</title>
<link rel="stylesheet" href="https://fonts.googleapis.com/css2?family=Oswald:wght@300;400&family=Open+Sans:wght@300;400;600&display=swap">
<style>
:root{
  --navy:#001c3f;
  --sky:#1ab0e8;
  --lime:#86bc24;
  --leaf:#4f8a0b;
  --leaf-dark:#3f7508;
  --ink:#222;
  --body:#555;
  --white:#fff;
}
*{margin:0;padding:0;box-sizing:border-box}
html,body{width:1120px;height:1200px;overflow:hidden}
body{position:relative;background:var(--white);font-family:"Open Sans",sans-serif;color:var(--body)}
.abs{position:absolute}
.top{left:0;top:0;width:1120px;height:583px;background:var(--navy)}
.brand{left:168px;top:10px;font-family:"Open Sans",sans-serif;font-weight:600;font-size:32px;color:var(--sky)}
.brand-dot{left:290px;top:14px;width:12px;height:12px;border-radius:50%;background:var(--lime)}
.collage{left:46px;top:67px;width:1026px;height:314px;
  background:linear-gradient(90deg,#b58a55 0%,#cfc4c8 18%,#7d5a2a 40%,#c85a1e 66%,#e58a2c 74%,#2ab7a6 86%,#4fa8c8 100%)}
.hero-box{left:166px;top:90px;width:506px;height:264px;
  background:radial-gradient(ellipse at 70% 80%,#6fb81c 0%,#3f8a10 55%,#1f5a08 100%);padding:28px 0 0 23px}
.hero-title{font-family:"Oswald",sans-serif;font-weight:400;font-size:56px;line-height:48px;color:var(--white);letter-spacing:.5px;text-transform:uppercase}
.hero-sub{margin-top:10px;font-weight:300;font-size:19px;line-height:19px;color:var(--white);width:460px}
.nav-arrow{top:182px;width:50px;height:50px;border-radius:50%;background:#3d8a0c}
.nav-arrow svg{position:absolute;top:17px}
.nav-prev{left:-26px}.nav-prev svg{left:29px}
.nav-next{left:1094px}.nav-next svg{left:13px}
.role-card{top:410px;width:400px}
.role-icon{position:absolute;left:0;top:0}
.role-title{position:absolute;left:89px;top:0;font-size:24px;color:var(--sky);font-weight:400}
.role-text{position:absolute;left:89px;top:28px;width:310px;font-size:13px;line-height:14.5px;color:var(--white)}
.socials{position:absolute;left:90px;top:69px;display:flex;gap:4px}
.socials span{width:19px;height:19px;border-radius:50%;background:var(--sky)}
.btn{position:absolute;left:92px;top:99px;width:125px;height:39px;border-radius:3px;
  background:linear-gradient(#8fc02a,#5f8f12);color:var(--white);font-weight:600;font-size:14px;
  display:flex;align-items:center;justify-content:center}
.section-title{left:0;width:1090px;top:608px;text-align:center;font-family:"Oswald",sans-serif;font-size:35px;color:var(--ink);letter-spacing:1px}
.track-title{top:672px;width:300px;text-align:center;font-family:"Oswald",sans-serif;font-weight:300;font-size:30px}
.pub{color:var(--lime)}.adv{color:var(--sky)}
.step{top:721px;width:100px;text-align:center;font-size:13.5px;line-height:14.5px}
.step .dot{width:62px;height:62px;border-radius:50%;margin:0 auto 8px;display:flex;align-items:center;justify-content:center;position:relative}
.step.pub .dot{background:var(--sky)}.step.adv .dot{background:var(--lime)}
.step.pub{color:var(--sky)}.step.adv{color:var(--leaf)}
.step .tail{position:absolute;left:60px;top:24px}
.copy{top:828px;font-size:13px;line-height:19.2px;color:var(--body)}
.story{left:0;top:1006px;width:1120px;height:138px;background:var(--leaf)}
.story h2{position:absolute;left:174px;top:30px;font-family:"Oswald",sans-serif;font-weight:300;font-size:30px;color:var(--white)}
.story p{position:absolute;left:176px;top:70px;width:780px;font-size:13.5px;line-height:19.2px;color:var(--white)}
.foot{left:0;top:1144px;width:1120px;height:56px;background:var(--navy)}
.foot-links{position:absolute;left:183px;top:19px;font-size:13.5px;color:var(--sky);display:flex;gap:13px}
.foot-links .copyright{color:var(--lime);margin-left:3px}
.foot-social{position:absolute;left:864px;top:14px;display:flex;gap:3px}
.foot-social span{width:26px;height:26px;border-radius:50%;background:var(--sky)}
</style>
</head>
<body>
<header class="abs top">
  <div class="abs brand">Chatterly</div>
  <div class="abs brand-dot"></div>
  <div class="abs collage" role="img" aria-label="Photo collage: a hand holding a seedling, joined hands, a building under construction, a car, a city skyline and a cup of coffee"></div>
  <div class="abs hero-box">
    <h1 class="hero-title">Chatterly is the<br>Rex Thunderton of<br>social traffic</h1>
    <p class="hero-sub">our publishers reach over 200 million unique consumers in 80 countries, impressed? Yeah that is kind of cool actually...</p>
  </div>
  <div class="abs nav-arrow nav-prev"><svg width="9" height="16" viewBox="0 0 9 16"><path d="M8 1L1 8l7 7" fill="none" stroke="#fff" stroke-width="2"/></svg></div>
  <div class="abs nav-arrow nav-next"><svg width="9" height="16" viewBox="0 0 9 16"><path d="M1 1l7 7-7 7" fill="none" stroke="#fff" stroke-width="2"/></svg></div>

  <div class="abs role-card" style="left:170px">
    <svg class="role-icon" width="95" height="130" viewBox="0 0 95 130">
      <circle cx="30" cy="20" r="17" fill="#1ab0e8"/>
      <path d="M0 78V56q0-16 16-16h28q16 0 16 16v22z" fill="#1ab0e8"/>
      <polygon points="60,33 68,40 79,40 79,51 86,59 79,67 79,78 68,78 60,85 52,78 41,78 41,67 34,59 41,51 41,40 52,40" fill="#001c3f" stroke="#fff" stroke-width="2"/>
      <path d="M54 51h9l4 4v12h-13z" fill="none" stroke="#fff" stroke-width="1.6"/>
      <path d="M57 59h7M57 63h7" stroke="#fff" stroke-width="1.4"/>
      <path d="M5 82q10 30 80 34" fill="none" stroke="#2aa12a" stroke-width="1.5"/>
      <path d="M84 110l8 6-8 5z" fill="#2aa12a"/>
    </svg>
    <div class="role-title">PUBLISHERS</div>
    <p class="role-text">Earn money posting sponsored tweets, lumiport updates and blog entries about things you love!.</p>
    <div class="socials"><span></span><span></span><span></span><span></span><span></span><span></span></div>
    <div class="btn">Sign up</div>
  </div>

  <div class="abs role-card" style="left:587px">
    <svg class="role-icon" width="95" height="130" viewBox="0 0 95 130">
      <circle cx="30" cy="20" r="17" fill="#1ab0e8"/>
      <path d="M0 78V56q0-16 16-16h28q16 0 16 16v22z" fill="#1ab0e8"/>
      <polygon points="60,33 68,40 79,40 79,51 86,59 79,67 79,78 68,78 60,85 52,78 41,78 41,67 34,59 41,51 41,40 52,40" fill="#001c3f" stroke="#fff" stroke-width="2"/>
      <path d="M52 56h4l10-6v18l-10-6h-4z" fill="#fff"/>
      <path d="M5 82q10 30 80 34" fill="none" stroke="#2aa12a" stroke-width="1.5"/>
      <path d="M84 110l8 6-8 5z" fill="#2aa12a"/>
    </svg>
    <div class="role-title">ADVERTISERS</div>
    <p class="role-text">Instantly create a campaign that millions of relevant consumers will see promoted by publishers they listen to and respect. Only pay for clicks based on your specific targeting criteria.</p>
    <div class="btn">Sign up</div>
  </div>
</header>

<main>
  <h2 class="abs section-title">HOW IT WORKS</h2>
  <svg class="abs" style="left:340px;top:650px" width="430" height="26" viewBox="0 0 430 26">
    <path d="M6 24V3h415v21" fill="none" stroke="#aaa" stroke-width="1"/>
    <path d="M3 20h6l-3 5zM418 20h6l-3 5z" fill="#aaa"/>
  </svg>
  <h3 class="abs track-title pub" style="left:194px">FOR PUBLISHERS</h3>
  <h3 class="abs track-title adv" style="left:608px">FOR ADVERTISERS</h3>

  <div class="abs step pub" style="left:154px"><div class="dot">
    <svg width="30" height="26" viewBox="0 0 30 26"><rect x="1" y="1" width="28" height="18" rx="2" fill="#fff"/><rect x="11" y="19" width="8" height="4" fill="#fff"/><rect x="7" y="23" width="16" height="2" fill="#fff"/></svg>
    <svg class="tail" width="18" height="14" viewBox="0 0 18 14"><path d="M0 4h9V0l9 7-9 7v-4H0z" fill="#1ab0e8"/></svg></div>Sign Up</div>
  <div class="abs step pub" style="left:251px"><div class="dot">
    <svg width="30" height="26" viewBox="0 0 30 26"><rect x="1" y="6" width="28" height="19" rx="3" fill="#fff"/><path d="M10 6V2h10v4" fill="none" stroke="#fff" stroke-width="2.5"/></svg>
    <svg class="tail" width="18" height="14" viewBox="0 0 18 14"><path d="M0 4h9V0l9 7-9 7v-4H0z" fill="#1ab0e8"/></svg></div>Pick Your<br>Products</div>
  <div class="abs step pub" style="left:348px"><div class="dot">
    <svg width="24" height="30" viewBox="0 0 24 30"><path d="M2 1h13l7 7v21H2z" fill="none" stroke="#fff" stroke-width="2.5"/><path d="M6 15h12M6 20h12M6 25h12" stroke="#fff" stroke-width="2"/></svg>
    <svg class="tail" width="18" height="14" viewBox="0 0 18 14"><path d="M0 4h9V0l9 7-9 7v-4H0z" fill="#1ab0e8"/></svg></div>Publish Your<br>Findings</div>
  <div class="abs step pub" style="left:444px"><div class="dot">
    <svg width="34" height="22" viewBox="0 0 34 22"><rect x="1" y="1" width="32" height="20" rx="2" fill="none" stroke="#fff" stroke-width="2.5"/><circle cx="17" cy="11" r="6" fill="#fff"/></svg></div>Make Money</div>

  <div class="abs step adv" style="left:563px"><div class="dot">
    <svg width="30" height="26" viewBox="0 0 30 26"><rect x="1" y="1" width="28" height="18" rx="2" fill="#fff"/><rect x="11" y="19" width="8" height="4" fill="#fff"/><rect x="7" y="23" width="16" height="2" fill="#fff"/></svg>
    <svg class="tail" width="18" height="14" viewBox="0 0 18 14"><path d="M0 4h9V0l9 7-9 7v-4H0z" fill="#86bc24"/></svg></div>Create an<br>Account</div>
  <div class="abs step adv" style="left:660px"><div class="dot">
    <svg width="28" height="28" viewBox="0 0 28 28"><circle cx="14" cy="14" r="13" fill="#fff"/><path d="M14 7v14M7 14h14" stroke="#86bc24" stroke-width="4"/></svg>
    <svg class="tail" width="18" height="14" viewBox="0 0 18 14"><path d="M0 4h9V0l9 7-9 7v-4H0z" fill="#86bc24"/></svg></div>Add Your<br>Content</div>
  <div class="abs step adv" style="left:756px"><div class="dot">
    <svg width="30" height="30" viewBox="0 0 30 30"><rect x="1" y="4" width="28" height="25" rx="2" fill="#fff"/><path d="M8 1v6M22 1v6" stroke="#fff" stroke-width="3"/><path d="M5 14h4M11 14h4M17 14h4M23 14h2M5 20h4M11 20h4M17 20h4M23 20h2" stroke="#86bc24" stroke-width="3"/></svg>
    <svg class="tail" width="18" height="14" viewBox="0 0 18 14"><path d="M0 4h9V0l9 7-9 7v-4H0z" fill="#86bc24"/></svg></div>Create a<br>Weekly Budget</div>
  <div class="abs step adv" style="left:853px"><div class="dot">
    <svg width="18" height="30" viewBox="0 0 18 30"><path d="M9 0v6" stroke="#fff" stroke-width="1.5"/><rect x="1" y="6" width="16" height="23" rx="8" fill="#fff"/><path d="M9 6v8" stroke="#86bc24" stroke-width="1.5"/></svg></div>Receive<br>Relevant Click</div>

  <p class="abs copy" style="left:173px;width:360px">Whether you have 100 friends/followers on lumiport and zonvel or 100,000+ you can earn great money posting fun and interesting content from brands and sites you already love and talk about anyway, so what are you waiting for?</p>
  <p class="abs copy" style="left:582px;width:372px">You want to reach relevant consumers right? Right. Well there's no better customer than one that was referred to you by someone they like and trust, that's a fact Jack. With Chatterly you can target huge audiences by interests and other demographics while only paying for clicks generated from a truly interested consumer and all at way lower costs per click than all other advertising options. Try it, you'll love it!</p>

  <section class="abs story">
    <h2>TRUE STORY</h2>
    <p>TuneFetch.io wanted to promote their new free app that allows users to download clipnest videos as music files. Chatterly traffic resulted in over 1.2 million interested clicks 400,000+ new downloads and thousands of lumiport likes and shares!</p>
  </section>
</main>

<footer class="abs foot">
  <nav class="foot-links"><span>FAQ</span><span>Terms</span><span>Privacy</span><span class="copyright">© 2013 chatterly. All rights reserved</span></nav>
  <div class="foot-social"><span></span><span></span><span></span></div>
</footer>
</body>
</html>
```